International PR and marketing agency needs website design

We need a branding website, for a company based in the US (Washington DC). We are a communication (PR, marketing, social media) agency. We already have the copy, and we have some example websites (some major agencies), that we like.
For example:
https://pellowtrask.example/
https://durnevaleglobal.example/
https://varnok.example/
https://qmf-reach.example/
https://www.thornbury.example/
The website must be a multi-language site, we will add the new languages step-by-step.
We would like to upload content continuously.
The website has to have sub-pages (segments), and news part.
Target Market(s)
Global
Industry/Entity Type
Public relations, Communications, Marketing, Social Media
Number of Pages Required
5+ page
Font styles to use
Other font styles liked:
- Well readable, modern style.
Look and feel

```html
<!DOCTYPE html>
<html lang="en">
<head>
<meta charset="utf-8">
<title>Vantara PR — Home</title>
<link href="https://fonts.googleapis.com/css2?family=Catamaran:wght@500;600;700&family=Poppins:wght@300;400;500;600&family=Rubik:wght@400;500&display=swap" rel="stylesheet">
<style>
:root{
  --ink:#0b0b0c;
  --brand:#c00c3a;
  --white:#ffffff;
  --text-dark:#1b1b22;
  --text-muted:#6d6d78;
  --card:#e2ebfb;
  --link:#2d6ee0;
  --hero-a:#141214;
  --hero-b:#3a3438;
}
*{margin:0;padding:0;box-sizing:border-box}
html,body{width:918px;height:1200px;overflow:hidden;background:var(--white)}
body{position:relative;font-family:"Poppins",sans-serif;color:var(--text-dark)}
.abs{position:absolute}

/* header */
.site-header{left:0;top:0;width:918px;height:81px;background:var(--ink)}
.header-rule{left:0;top:48px;width:918px;height:1px;background:#1f1f22}
.brand{left:186px;top:22px;font-family:"Catamaran",sans-serif;font-weight:700;font-size:22px;color:var(--brand);display:flex;align-items:center;gap:6px;white-space:nowrap}
.brand-dot{width:10px;height:10px;border-radius:50%;background:var(--brand)}
.main-nav{top:0;left:0;height:48px}
.main-nav a{position:absolute;top:18px;font-family:"Catamaran",sans-serif;font-weight:600;font-size:8.5px;color:var(--white);text-decoration:none;white-space:nowrap}
.nav-active{left:323px;top:46px;width:49px;height:2px;background:var(--brand)}
.utility-bar{left:630px;top:0;width:288px;height:48px}
.util-divider{top:0;width:1px;height:48px;background:rgba(255,255,255,.18)}
.social-dot{top:19px;width:9px;height:9px;border-radius:50%;border:1.2px solid rgba(255,255,255,.55)}
.social-dot.active{border-color:var(--white)}

/* hero */
.hero{left:0;top:81px;width:918px;height:408px;background:linear-gradient(100deg,var(--hero-a) 0%,#0f0d0f 45%,var(--hero-b) 78%,#221e22 100%)}
.hero-eyebrow{left:180px;top:180px;font-family:"Catamaran",sans-serif;font-weight:500;font-size:9px;color:var(--white)}
.hero-title{left:178px;top:203px;font-family:"Catamaran",sans-serif;font-weight:700;font-size:37px;line-height:46px;color:var(--white)}
.hero-cta{left:180px;top:361px;width:95px;height:33px;background:var(--brand);color:var(--white);font-family:"Catamaran",sans-serif;font-weight:600;font-size:8px;display:flex;align-items:center;justify-content:center}

/* about */
.about-photo{left:125px;top:537px;width:303px;height:255px;border-radius:5px;background:linear-gradient(135deg,#d9dde0 0%,#8d8f92 50%,#3d6a4a 100%)}
.eyebrow{left:469px;top:572px;font-size:10px;font-weight:600;letter-spacing:2px;color:var(--brand)}
.about-title{left:469px;top:588px;font-size:30px;font-weight:600;color:var(--text-dark)}
.about-copy{left:469px;width:330px;font-size:9.2px;font-weight:300;line-height:15.3px;color:var(--text-muted)}

/* expertise */
.expertise-title{left:0;top:870px;width:944px;text-align:center;font-family:"Rubik",sans-serif;font-weight:500;font-size:31px;line-height:38px;color:var(--text-dark)}
.service-icon{left:119px;width:67px;height:67px;border-radius:50%}
.service-title{left:206px;font-family:"Rubik",sans-serif;font-weight:500;font-size:16px;letter-spacing:.3px;color:var(--text-dark)}
.service-copy{left:206px;font-family:"Rubik",sans-serif;font-size:10px;line-height:15.3px;letter-spacing:.2px;color:var(--text-muted)}
.feature-card{left:482px;top:987px;width:346px;height:186px;border-radius:14px;background:var(--card)}
.feature-title{left:508px;top:1016px;font-family:"Rubik",sans-serif;font-weight:500;font-size:20.5px;color:var(--text-dark);white-space:nowrap}
.feature-copy{left:508px;top:1054px;width:250px;font-family:"Rubik",sans-serif;font-size:10px;line-height:15.4px;color:var(--text-muted)}
.feature-link{left:508px;top:1124px;font-family:"Rubik",sans-serif;font-weight:500;font-size:10.5px;color:var(--link);display:flex;align-items:center;gap:10px}
</style>
</head>
<body>

<header class="abs site-header">
  <div class="abs header-rule"></div>
  <nav class="abs main-nav">
    <a style="left:330px">Home +</a>
    <a style="left:379px">About Us</a>
    <a style="left:433px">Our Work</a>
    <a style="left:489px">Phylosophy</a>
    <a style="left:552px">Contact</a>
    <a style="left:602px">Practice</a>
  </nav>
  <div class="abs nav-active"></div>
  <svg class="abs" style="left:630px;top:0" width="288" height="48" aria-hidden="true">
    <polygon points="0,0 288,0 288,48 16,48" fill="var(--brand)"/>
  </svg>
  <div class="abs utility-bar">
    <div class="abs social-dot" style="left:34px"></div>
    <div class="abs social-dot active" style="left:70px"></div>
    <div class="abs social-dot" style="left:105px"></div>
    <div class="abs util-divider" style="left:134px"></div>
    <svg class="abs" style="left:144px;top:16px" width="14" height="14" aria-hidden="true">
      <circle cx="6" cy="6" r="4.6" fill="none" stroke="rgba(255,255,255,.6)" stroke-width="1"/>
      <line x1="9.4" y1="9.4" x2="13" y2="13" stroke="rgba(255,255,255,.6)" stroke-width="1"/>
    </svg>
    <div class="abs util-divider" style="left:172px"></div>
    <svg class="abs" style="left:182px;top:17px" width="13" height="13" aria-hidden="true">
      <g fill="none" stroke="#fff" stroke-width="1">
        <rect x=".5" y=".5" width="4.8" height="4.8" rx="1"/><rect x="7.5" y=".5" width="4.8" height="4.8" rx="1"/>
        <rect x=".5" y="7.5" width="4.8" height="4.8" rx="1"/><rect x="7.5" y="7.5" width="4.8" height="4.8" rx="1"/>
      </g>
    </svg>
  </div>
</header>

<section class="abs hero" role="img" aria-label="Dark photo of a businessman in a suit holding a small figure, with silhouettes of people below"></section>
<svg class="abs" style="left:0;top:81px" width="918" height="408" aria-hidden="true">
  <circle cx="0" cy="73" r="22" fill="var(--brand)"/>
  <path d="M0,216 C40,236 80,232 110,262 C150,300 160,350 190,408" fill="none" stroke="var(--brand)" stroke-width="3"/>
  <circle cx="57" cy="220" r="11" fill="none" stroke="rgba(255,255,255,.12)" stroke-width="1"/>
  <g stroke="#fff" stroke-width="1.2" fill="none"><line x1="33" y1="220" x2="57" y2="220"/><polyline points="40,213 33,220 40,227"/></g>
  <circle cx="862" cy="221" r="11" fill="none" stroke="#6b3ad8" stroke-width="1"/>
  <g stroke="#8a49e6" stroke-width="1.2" fill="none"><line x1="862" y1="221" x2="886" y2="221"/><polyline points="879,214 886,221 879,228"/></g>
</svg>
<div class="abs brand"><span class="brand-dot"></span>Vantara PR</div>
<p class="abs hero-eyebrow">Calder Business House.</p>
<h1 class="abs hero-title">We Are Building<br>Relationships</h1>
<a class="abs hero-cta">Discover More +</a>

<div class="abs about-photo" role="img" aria-label="Photo of four colleagues gathered around a laptop in a bright office"></div>
<p class="abs eyebrow">ABOUT US</p>
<h2 class="abs about-title">About Lumora</h2>
<p class="abs about-copy" style="top:647px">Lorem ipsum dolor sit amet, consectetur adipiscing elit. Suspendisse nec turpis mi. Sed varius ligula at lorem finibus molestie. Pellentesque vel orci et ligula egestas dapibus. Sed quis orci eget lorem porttitor fermentum quis vitae lacus.</p>
<p class="abs about-copy" style="top:728px">Consectetur adipiscing elit. Suspendisse nec turpis mi. Sed varius ligula at lorem finibus molestie. Pellentesque vel orci et ligula egestas dapibus.</p>

<h2 class="abs expertise-title">Our Expertise Includes<br>Digital Value Chain</h2>

<div class="abs service-icon" style="top:992px;background:linear-gradient(135deg,#fbd2c0,#f29aa6 55%,#6d4bd8)" role="img" aria-label="Illustration of a growth chart on a laptop"></div>
<h3 class="abs service-title" style="top:988px">Investment Strategy</h3>
<p class="abs service-copy" style="top:1015px">A sharp expertise of a consulting firm<br>combined<br>with the agility of startups.</p>

<div class="abs service-icon" style="top:1105px;background:linear-gradient(135deg,#f7c8cf,#ef8a8a 50%,#4a2c5e)" role="img" aria-label="Illustration of a person using a phone beside a laptop"></div>
<h3 class="abs service-title" style="top:1100px">Customer Journey</h3>
<p class="abs service-copy" style="top:1127px">A sharp expertise of a consulting firm<br>combined<br>with the agility of startups.</p>

<div class="abs feature-card"></div>
<h3 class="abs feature-title">Digital Strategy &amp; Innovation</h3>
<p class="abs feature-copy">At vero eos et ultimum bonorum, quod omnium philosophorum sententia tale debet esse, ut aut fugiat aliquid, praeter voluptatem ut de quo.</p>
<a class="abs feature-link">Get started now
  <svg width="12" height="10" aria-hidden="true"><g stroke="var(--link)" stroke-width="1.5" fill="none"><line x1="0" y1="5" x2="11" y2="5"/><polyline points="7,1 11,5 7,9"/></g></svg>
</a>

</body>
</html>
```